Silver Hollow is a cabin in Gatlinburg, Tennessee, near the Pinecrest Ridge National Park. When our cabin was built, there was one thing more important than any other--peace. The front of our cabin is surrounded by woods. It has a huge deck with a swing, Adirondack chairs, and a love seat for relaxation. The back deck has a hot tub, a large round glass table for cocktails or dinner, and because we left no stone unturned, we have a telescope for stargazing. There are two master suites, each have a private bath with a large jetted tub, seperate shower, flat screen TV, and a door that leads to the back deck.

Contact Information for Business Card

Silver Hollow Vacation Rentals, LLC
817 Harlow Brook Ct.
Oakland, Ky 40000
Janet M. Colbert, Owner/Manager
(270) 555.0147

```html
<!DOCTYPE html>
<html lang="en">
<head>
<meta charset="utf-8">
<title>Silver Hollow Vacation Rentals, LLC — Business Card</title>
<link rel="stylesheet" href="https://fonts.googleapis.com/css2?family=Fondamento:ital@1&family=Archivo+Black&family=Libre+Baskerville&family=Old+Standard+TT&display=swap">
<style>
  :root {
    --forest-green: #1d6a1f;
    --icon-green: #14661a;
    --ink: #0d0d0d;
    --canopy-light: #eef3e6;
    --canopy-mid: #a9c59a;
    --canopy-deep: #6f8f68;
    --trunk: #7d786a;
  }
  html, body {
    margin: 0;
    padding: 0;
    width: 1200px;
    height: 702px;
    overflow: hidden;
    background: #ffffff;
  }
  .business-card {
    position: relative;
    width: 1200px;
    height: 702px;
    overflow: hidden;
  }
  .forest-backdrop {
    position: absolute;
    inset: 0;
    background:
      radial-gradient(ellipse 320px 220px at 230px 40px, rgba(255,255,250,0.95), rgba(255,255,250,0) 75%),
      radial-gradient(ellipse 170px 520px at 620px 560px, rgba(125,120,106,0.75), rgba(125,120,106,0) 80%),
      radial-gradient(ellipse 140px 480px at 1060px 480px, rgba(130,128,110,0.55), rgba(130,128,110,0) 80%),
      linear-gradient(180deg, var(--canopy-light) 0%, var(--canopy-mid) 35%, var(--canopy-deep) 100%);
  }
  .forest-backdrop::after {
    content: "";
    position: absolute;
    inset: 0;
    background: rgba(255,255,255,0.28);
  }
  .company-name {
    position: absolute;
    top: 62px;
    left: 0;
    width: 1200px;
    margin: 0;
    text-align: center;
    font-family: "Fondamento", "Georgia", serif;
    font-style: italic;
    font-weight: 400;
    font-size: 47px;
    letter-spacing: 1px;
    color: var(--forest-green);
  }
  .owner-name {
    position: absolute;
    top: 262px;
    left: 0;
    width: 1172px;
    margin: 0;
    text-align: center;
    font-family: "Archivo Black", "Arial Black", sans-serif;
    font-size: 46px;
    font-weight: 400;
    color: var(--ink);
  }
  .owner-title {
    position: absolute;
    top: 336px;
    left: 0;
    width: 1172px;
    margin: 0;
    text-align: center;
    font-family: "Old Standard TT", "Times New Roman", serif;
    font-size: 25px;
    color: var(--forest-green);
  }
  .contact-line {
    position: absolute;
    left: 72px;
    display: flex;
    align-items: center;
    font-family: "Libre Baskerville", "Bookman Old Style", serif;
    font-size: 40px;
    color: var(--ink);
    white-space: nowrap;
  }
  .contact-line svg { flex: none; }
  .contact-phone { top: 474px; }
  .contact-phone svg { margin: 0 28px 0 14px; }
  .contact-address { top: 568px; }
  .contact-address svg { margin-right: 24px; }
</style>
</head>
<body>
  <main class="business-card">
    <div class="forest-backdrop" role="img" aria-label="Photograph looking up at tall mossy forest trees with sunlight through the canopy"></div>

    <h1 class="company-name">Silver Hollow Vacation Rentals, LLC</h1>

    <p class="owner-name">Janet M. Colbert</p>
    <p class="owner-title">Owner / Manager</p>

    <p class="contact-line contact-phone">
      <svg width="46" height="66" viewBox="0 0 46 66" aria-hidden="true">
        <path fill="var(--icon-green)" d="M8 2 L18 0 L23 17 L15 22 C14 32 19 44 27 52 L35 47 L45 60 L37 66 C22 66 4 44 2 22 C1 12 3 6 8 2 Z"/>
      </svg>
      (270) 555.0147
    </p>

    <p class="contact-line contact-address">
      <svg width="72" height="58" viewBox="0 0 72 58" aria-hidden="true">
        <path fill="var(--icon-green)" d="M36 0 L72 17 L72 25 L36 9 L0 25 L0 17 Z"/>
        <path fill="var(--icon-green)" d="M10 24 L36 13 L62 24 L62 58 L10 58 Z"/>
      </svg>
      817 Harlow Brook Ct. Oakland, Ky 40000
    </p>
  </main>
</body>
</html>
```